Business card required for IT Consultancy Business - Tealbrook Consulting.
Company provides the whole nine yards of services across IT Architecture, design and execution.
Basically we provide consulting services to help businesses make sure their technology is enabling their business strategy.
Design for front and back required.
We would like the front of the card to inlcude:
Name
Title
Mobile number
email address
www.tbkc.com.au
Company logos attached.
Thank you
Industry/Entity Type
Business
Contact Information for Business Card
Name
Title
Mobile number
email address
www.tbkc.com.au
Look and feel
Each slider illustrates characteristics of the customer's brand and the style your logo design should communicate.

```html
<!DOCTYPE html>
<html lang="en">
<head>
<meta charset="utf-8">
<title>Tealbrook Consulting – Business Card</title>
<link href="https://fonts.googleapis.com/css2?family=Open+Sans:wght@400;600;700&display=swap" rel="stylesheet">
<style>
  :root {
    --backdrop: #2b2b2d;
    --card-white: #fbfbfb;
    --brand-orange: #e8532a;
    --brand-blue: #1f6fb8;
    --ink: #3a3a3a;
    --on-orange: #ffffff;
  }
  * { box-sizing: border-box; margin: 0; padding: 0; }
  html, body {
    width: 1200px; height: 960px; overflow: hidden;
    background: var(--backdrop);
    font-family: "Open Sans", Arial, sans-serif;
  }
  .canvas {
    position: relative; width: 1200px; height: 960px;
  }
  .card {
    position: absolute; left: 250px; width: 700px; height: 400px;
    box-shadow: 0 10px 30px rgba(0,0,0,.45);
  }
  /* Back side */
  .card--back {
    top: 50px; background: var(--brand-orange);
    display: flex; flex-direction: column; align-items: center; justify-content: center;
  }
  .card--back .wordmark { color: var(--on-orange); }
  .card--back .web {
    position: absolute; bottom: 26px; left: 0; right: 0; text-align: center;
    color: var(--on-orange); font-size: 13px; letter-spacing: 5px; opacity: .85;
  }
  /* Front side */
  .card--front { top: 500px; background: var(--card-white); }
  .card--front .wordmark {
    position: absolute; top: 80px; right: 48px; color: var(--brand-blue);
  }
  .wordmark {
    display: flex; align-items: center; gap: 12px;
    font-weight: 700; font-size: 38px; letter-spacing: .5px; line-height: 1;
  }
  .wordmark .dot {
    width: 20px; height: 20px; border-radius: 50%; background: currentColor;
  }
  .accent {
    position: absolute; left: 0; top: 206px; width: 12px;
  }
  .accent__orange { height: 40px; background: var(--brand-orange); }
  .accent__blue { height: 82px; background: var(--brand-blue); }
  .contact {
    position: absolute; left: 36px; top: 210px;
  }
  .contact__name {
    color: var(--brand-blue); font-weight: 700; font-size: 17px; letter-spacing: .3px;
  }
  .contact__title {
    color: var(--brand-orange); font-weight: 600; font-size: 16px; margin-bottom: 10px;
  }
  .contact__list { list-style: none; }
  .contact__list li {
    display: flex; align-items: center; gap: 10px;
    color: var(--ink); font-size: 15px; line-height: 23px;
  }
  .contact__list svg { width: 13px; height: 13px; fill: var(--brand-blue); flex: none; }
</style>
</head>
<body>
<main class="canvas">
  <section class="card card--back" aria-label="Card back">
    <div class="wordmark"><span class="dot"></span>Tealbrook Consulting</div>
    <p class="web">www.tbkc.com.au</p>
  </section>

  <section class="card card--front" aria-label="Card front">
    <div class="wordmark"><span class="dot"></span>Tealbrook Consulting</div>
    <div class="accent">
      <div class="accent__orange"></div>
      <div class="accent__blue"></div>
    </div>
    <div class="contact">
      <p class="contact__name">MAYA ELLISON</p>
      <p class="contact__title">CEO/FOUNDER</p>
      <ul class="contact__list">
        <li>
          <svg viewBox="0 0 16 16" aria-hidden="true"><path d="M4 0h8a1 1 0 0 1 1 1v14a1 1 0 0 1-1 1H4a1 1 0 0 1-1-1V1a1 1 0 0 1 1-1zm1 2v10h6V2zm3 11a1 1 0 1 0 0 2 1 1 0 0 0 0-2z"/></svg>
          412 305 7781
        </li>
        <li>
          <svg viewBox="0 0 16 16" aria-hidden="true"><path d="M0 3h16v10H0zm1.5 1.2V5l6.5 4 6.5-4v-.8L8 8.2z"/></svg>
          maya@tbkc.com.au
        </li>
        <li>
          <svg viewBox="0 0 16 16" aria-hidden="true"><circle cx="8" cy="8" r="8"/></svg>
          www.tbkc.com.au
        </li>
      </ul>
    </div>
  </section>
</main>
</body>
</html>
```